Lanterns Valley Foundation Web Design

The design we need is for a WordPress blog that will be our content platform. We are a registered 501(c)3 non-profit that focuses on financially supporting the treatment of cancer patients that have been told they have no hope and there is nothing the conventional medical system can do for them. Through this wesbite we want to both rasie awareness about the treatment options plus, raise funds for treating patients. The two primary target audiences of the site are...

1. Terminally ill patients and their families to let them know that there is an option other then hospice and that we are hear to support that option.

2. People looking to help donate to a worthwhile cause that resonates with them.

The website is https://lanternsvalleyfoundation.org/

See attached logo designs!!!

Target Market(s)

Cancer patients and their families

Industry/Entity Type

Foundation

Font styles to use
Sans Serif

Colors
ffffff
fbed22

Requirements
Must have
• I like this look of this site. It is clean, simple, helpful, soft. I like the flow of the pages.
• http://www.brightpathgiving.org/
• I like the design and flow but NOT the color or boldness
• https://tqsn-youth.org/
• I like this style for a donation page.
• https://www.healingscience.org/we-are-hsa/join-the-cause/donations/one-time-donation
• with the addition of a Would you like your employer to match? button.
Nice to have
• White black and gold - but soft
• Even possibly grayscale like the site I like.

```html
<!DOCTYPE html>
<html lang="en">
<head>
<meta charset="utf-8">
<title>Lanterns Valley Foundation</title>
<link rel="stylesheet" href="https://fonts.googleapis.com/css2?family=Questrial&display=swap">
<style>
:root{
  --gold:#ecc75a;
  --gold-deep:#e2b94a;
  --ink:#2b2b2b;
  --text:#3a3a3a;
  --muted:#6b6b6b;
  --paper:#ffffff;
  --wash:#f5f5f5;
  --line:#e3e3e3;
  --banner:#a9adbd;
}
*{margin:0;padding:0;box-sizing:border-box}
html,body{width:1200px;height:2281px;overflow:hidden}
body{position:relative;background:var(--paper);font-family:"Questrial",sans-serif;color:var(--text)}
.abs{position:absolute}
.top-rule{left:0;top:0;width:1200px;height:4px;background:var(--gold)}
.site-header{left:0;top:4px;width:1200px;height:104px;background:var(--paper);box-shadow:0 1px 3px rgba(0,0,0,.08);z-index:2}
.brand{left:161px;top:26px;display:flex;align-items:center;gap:12px}
.brand-mark{width:20px;height:20px;background:var(--gold)}
.brand-name{font-size:20px;line-height:24px;color:var(--ink);width:170px}
.call{left:783px;top:22px;font-size:14px;color:var(--ink)}
.call span{color:var(--gold)}
.donate{left:955px;top:13px;width:84px;height:33px;border:1.5px solid var(--gold);color:var(--gold);font-size:12px;display:flex;align-items:center;justify-content:center;letter-spacing:.5px}
.nav{top:70px;font-size:13px;color:var(--ink)}
.nav.active{color:var(--gold)}
.hero{left:0;top:108px;width:1200px;height:481px;background:linear-gradient(90deg,#efe2dc 0%,#f3e6e2 45%,#eedcd6 100%)}
.hero-card{left:161px;top:186px;width:324px;height:325px;background:var(--gold);padding:52px 34px 0}
.hero-card h1{font-weight:400;font-size:27px;line-height:39px;color:#fff}
.hero-card p{margin-top:18px;font-size:12.5px;line-height:24px;color:#fff}
.hero-btn{left:201px;top:426px;width:152px;height:39px;border:1.5px solid #fff;border-radius:20px;color:#fff;font-size:11.5px;display:flex;align-items:center;justify-content:center;letter-spacing:.5px}
.arrow{width:32px;height:32px;border:1.5px solid rgba(255,255,255,.9);border-radius:50%}
.dot{top:543px;width:12px;height:12px;border-radius:50%;background:#fff}
.dot.on{background:var(--gold)}
.wash{left:0;top:589px;width:1200px;height:1294px;background:var(--wash)}
.welcome{left:0;top:626px;width:1200px;text-align:center;font-size:24px;color:var(--ink)}
.card-img{top:689px;width:274px;height:175px}
.card-title{top:880px;width:274px;text-align:center;font-size:17px;color:var(--gold)}
.card-text{top:914px;width:274px;text-align:center;font-size:13px;line-height:25px;color:var(--text)}
.banner{left:161px;top:1004px;width:876px;height:398px;background:linear-gradient(90deg,#a7abbc 0%,#aeb0be 45%,#c9c0c0 75%,#ddd3d0 100%)}
.banner h2{left:225px;top:1142px;font-weight:400;font-size:24px;line-height:34px;color:#fff}
.banner-btn{left:221px;top:1227px;width:191px;height:49px;background:var(--gold);color:#fff;font-size:14px;letter-spacing:.5px;display:flex;align-items:center;justify-content:center}
.who{left:161px;top:1477px;width:333px;height:338px;background:var(--paper);padding:42px 26px 0}
.who h2{font-weight:400;font-size:26px;color:var(--ink)}
.who .lead{margin-top:18px;font-size:16.5px;line-height:26px;color:var(--gold)}
.who .body{margin-top:18px;font-size:13px;line-height:24px;color:var(--text)}
.who .more{margin-top:22px;font-size:14px;color:var(--gold)}
.who-img{left:497px;top:1477px;width:542px;height:338px;background:linear-gradient(90deg,#dfe4e6 0%,#c9d6d8 45%,#6f86a6 75%,#3d5f8f 100%)}
.call-band{left:0;top:1883px;width:1200px;height:100px;background:linear-gradient(90deg,#ebc257 0%,#f0cd5e 40%,#e7bd50 100%);display:flex;align-items:center;justify-content:center;gap:12px;color:#fff;font-size:22px}
.foot-head{top:2020px;font-size:13px;color:var(--ink);letter-spacing:.3px}
.foot-list{list-style:none;font-size:11.5px;color:var(--ink);line-height:26px}
.social{left:709px;top:2056px;display:flex;gap:16px;align-items:center}
.social .dot-icon{width:20px;height:20px;border-radius:50%;background:var(--ink)}
.foot-rule{left:161px;top:2218px;width:878px;height:1px;background:var(--line)}
.copyright{left:0;top:2243px;width:1200px;text-align:center;font-size:11.5px;color:var(--ink)}
</style>
</head>
<body>
<div class="abs top-rule"></div>
<header class="abs site-header">
  <div class="abs brand"><span class="brand-mark"></span><span class="brand-name">Lanterns Valley Foundation</span></div>
  <div class="abs call">CALL US: <span>555-210-7789</span></div>
  <div class="abs donate">DONATE</div>
  <nav>
    <span class="abs nav active" style="left:531px">Home</span>
    <span class="abs nav" style="left:613px">About us</span>
    <span class="abs nav" style="left:707px">Who we are</span>
    <span class="abs nav" style="left:823px">Funds</span>
    <span class="abs nav" style="left:900px">Blog</span>
    <span class="abs nav" style="left:973px">Contact us</span>
  </nav>
</header>

<section class="abs hero" role="img" aria-label="Photo of smiling women wearing pink awareness ribbons"></section>
<div class="abs hero-card">
  <h1>Lanterns Valley<br>Foundation</h1>
  <p>Sed ut perspiciatis unde omnis iste nat<br>onsit voluptatem accusantium doloreue<br>laudantium totam rem.</p>
</div>
<div class="abs hero-btn">FIND OUT MORE</div>
<svg class="abs arrow" style="left:37px;top:332px" viewBox="0 0 32 32"><path d="M18 10l-6 6 6 6" fill="none" stroke="#fff" stroke-width="1.6"/></svg>
<svg class="abs arrow" style="left:1126px;top:332px" viewBox="0 0 32 32"><path d="M14 10l6 6-6 6" fill="none" stroke="#fff" stroke-width="1.6"/></svg>
<span class="abs dot" style="left:566px"></span>
<span class="abs dot" style="left:584px"></span>
<span class="abs dot on" style="left:602px"></span>
<span class="abs dot" style="left:621px"></span>

<div class="abs wash"></div>
<h2 class="abs welcome" style="font-weight:400">Welcome to Lanterns Valley Foundation</h2>

<div class="abs card-img" style="left:161px;background:linear-gradient(135deg,#e8dcd6,#f1ebe8 60%,#c9c4c4)" role="img" aria-label="Photo of a patient resting in a hospital bed"></div>
<div class="abs card-img" style="left:464px;background:linear-gradient(135deg,#f6e9ec,#f3d9d8 50%,#f7eef0)" role="img" aria-label="Photo of cupped hands holding a pink ribbon"></div>
<div class="abs card-img" style="left:765px;background:linear-gradient(135deg,#8fa36a,#c7ccc6 50%,#3d4f67)" role="img" aria-label="Photo of a patient resting on a sofa"></div>
<div class="abs card-title" style="left:161px">Finibus Bonorum</div>
<div class="abs card-title" style="left:464px">Finibus Bonorum</div>
<div class="abs card-title" style="left:765px">Finibus Bonorum</div>
<p class="abs card-text" style="left:161px">Sed ut perspiciatis unde omnissitlup<br>tem accusantium dolorem.</p>
<p class="abs card-text" style="left:464px">Sed ut perspiciatis unde omnissitlup<br>tem accusantium doloremqloue</p>
<p class="abs card-text" style="left:765px">Sed ut perspiciatis unde omnissitlup<br>tem accusantium doloremqlou.</p>

<div class="abs banner" role="img" aria-label="Photo of a patient in a headscarf embraced by a younger woman"></div>
<h2 class="abs banner" style="background:none;width:auto;height:auto;left:225px;top:1142px;font-weight:400;font-size:24px;line-height:34px;color:#fff">We Are Registered 501(c)3<br>non-profit organisations</h2>
<div class="abs banner-btn">REGISTERED HERE</div>

<section class="abs who">
  <h2>Who We Are</h2>
  <p class="lead">Raise awareness about the<br>treatment options plus, raise<br>funds for treating patients</p>
  <p class="body">Sed ut perspiciatis unde omnissit voluptat em<br>accusantium doloremqloue udant lorium,<br>totam rem aperiam, eaqueuaeab</p>
  <p class="more">Read More</p>
</section>
<div class="abs who-img" role="img" aria-label="Video still of a young patient with a nurse"></div>
<svg class="abs" style="left:731px;top:1610px" width="72" height="72" viewBox="0 0 72 72"><circle cx="36" cy="36" r="34" fill="none" stroke="#fff" stroke-width="3"/><path d="M29 22l21 14-21 14z" fill="#fff"/></svg>

<div class="abs call-band">
  <svg width="28" height="28" viewBox="0 0 24 24"><path d="M6.6 3.5l2.6 3.3-1.6 2.2c1 2.2 3 4.2 5.3 5.3l2.2-1.6 3.3 2.6-1.5 3.2C11 18.5 5.5 13 4.3 5z" fill="none" stroke="#fff" stroke-width="1.3" stroke-linejoin="round"/></svg>
  <span>Call us on 555 318 6620</span>
</div>

<footer>
  <div class="abs foot-head" style="left:161px">ABOUT</div>
  <ul class="abs foot-list" style="left:161px;top:2050px"><li>Refer</li><li>Careers</li><li>News</li><li>Non Profit</li><li>Contact</li></ul>
  <div class="abs foot-head" style="left:297px">INFORMATION</div>
  <ul class="abs foot-list" style="left:297px;top:2050px"><li>Target patients</li><li>Organisation</li><li>Sed uerspiciatiem</li><li>Comnisteatusit</li><li>Perspiciatis unde</li></ul>
  <div class="abs foot-head" style="left:514px">WHO WE ARE</div>
  <ul class="abs foot-list" style="left:514px;top:2050px"><li>Sed utserspiciatis</li><li>Donate</li><li>Perspiciatis unde</li><li>Sed uerspiciatiem</li><li>Comnisteatusit</li></ul>
  <div class="abs foot-head" style="left:709px">CONNECT</div>
  <div class="abs social">
    <svg width="24" height="18" viewBox="0 0 24 18"><rect x="1" y="1" width="22" height="16" fill="var(--ink)"/><path d="M1 1l11 9 11-9M1 17l8-7M23 17l-8-7" fill="none" stroke="#fff" stroke-width="1.4"/></svg>
    <span class="dot-icon"></span><span class="dot-icon"></span><span class="dot-icon"></span>
  </div>
  <div class="abs foot-head" style="left:709px;top:2109px">POLICIES</div>
  <ul class="abs foot-list" style="left:709px;top:2138px"><li>Privacy</li><li>Complaint and Feedback</li></ul>
  <div class="abs foot-head" style="left:926px">OTHER LINKS</div>
  <ul class="abs foot-list" style="left:926px;top:2050px"><li>Sed utserspiciatis</li><li>Healthcare</li><li>Perspiciatis unde</li><li>Sed uerspiciatiem</li><li>Comnisteatusit</li></ul>
  <div class="abs foot-rule"></div>
  <p class="abs copyright">© 2017 Lanterns Valley Foundation. Privacy Policy &nbsp;|&nbsp; Terms of Use &nbsp;|&nbsp; Contact</p>
</footer>
</body>
</html>
```